Free Printer Promotion

Hi i need a banner AD for my website.

The promotion is: free printer, for a monthly cost you get all the supplies and service included. Its a subscription service for printing. There is 5 plans available.
Prices vary upon printers, most expensive plan is $69.94 a month for a 1 year term and the most affordable plan is $9.95 a month for 3 year term

1 Monochrome laser (print only printer, black and white printing)
2 Multifunction Monochrome laser (print scan copy fax printer, black and white printing)

• Monochrome Printers are given 1000 prints per month
• Toner included
• Service included
• Printer included

3 Color laser (print only printer, color printing)
4 Multifunction Color laser (print scan copy fax, color printing)
Color printers are given 500 monochrome prints and 500 color prints per month
• Toner included
• Service included
• Printer included

5 Inkjet color printer (print copy scan fax, color printing)
• Inkjet Printers are given 1000 prints per month.
• Ink included
• Service included
• Printer included

Target Market(s)

students, home office workers, corporate business and government

Font styles to use
Serif
Sans Serif

Requirements
Must have
• i want it to be enticing, no long sentences. the customer will click on the banner and it will bring them to another page with the information.

Keep it short and sweet.

```html
<!DOCTYPE html>
<html lang="en">
<head>
<meta charset="utf-8">
<title>Free Printers – Banner Set</title>
<link rel="stylesheet" href="https://fonts.googleapis.com/css2?family=Barlow+Condensed:wght@500&family=Montserrat:ital,wght@0,600;1,600;1,700&family=Poppins:wght@600&display=swap">
<style>
  :root {
    --blue: #2e85b4;
    --bright-blue: #1f9be0;
    --red: #ea1c2a;
    --ink: #111111;
    --white: #ffffff;
    --label: #222222;
    --sheet-top: #f1f5f4;
    --sheet-bottom: #c9e7df;
  }
  * { box-sizing: border-box; margin: 0; padding: 0; }
  html, body { width: 1152px; height: 1200px; overflow: hidden; }
  body {
    background: linear-gradient(160deg, var(--sheet-top) 0%, #e4f3ef 55%, var(--sheet-bottom) 100%);
    font-family: "Montserrat", Arial, sans-serif;
  }
  .sheet {
    position: absolute; left: 0; top: 0;
    width: 868px; height: 904px;
    transform: scale(1.3272);
    transform-origin: 0 0;
  }
  .size-label {
    position: absolute;
    font: 500 12px "Montserrat", Arial, sans-serif;
    color: var(--label);
  }
  .banner {
    position: absolute;
    background: var(--white);
    overflow: hidden;
    box-shadow: 4px 5px 6px rgba(0,0,0,0.28);
  }
  .banner .wave { position: absolute; left: 0; top: 0; width: 100%; height: 100%; }
  .wave path { fill: var(--blue); }

  .ribbon {
    position: absolute;
    background: var(--red);
    color: var(--white);
    font-family: "Montserrat", Arial, sans-serif;
    font-weight: 700;
    font-style: italic;
    text-align: center;
    transform-origin: center;
    white-space: nowrap;
  }
  .price {
    position: absolute;
    font-family: "Barlow Condensed", "Arial Narrow", sans-serif;
    font-weight: 500;
    color: var(--white);
    line-height: 1;
  }
  .term {
    position: absolute;
    font-style: italic;
    font-weight: 700;
    line-height: 1.25;
    white-space: nowrap;
  }
  .headline {
    position: absolute;
    font-family: "Barlow Condensed", "Arial Narrow", sans-serif;
    font-weight: 500;
    color: var(--ink);
    line-height: 1;
    white-space: nowrap;
  }
  .headline .accent { color: var(--bright-blue); }
  .subline {
    position: absolute;
    font-style: italic;
    font-weight: 700;
    color: #333;
    line-height: 1.3;
    white-space: nowrap;
  }
  .printer-photo {
    position: absolute;
    border-radius: 4px 4px 2px 2px;
    background: linear-gradient(180deg, #3a3a3a 0%, #3a3a3a 14%, #f4f4f4 15%, #e6e6e6 100%);
  }
  .cta {
    position: absolute;
    display: flex; align-items: center; justify-content: center;
    border: 2px solid var(--white);
    border-radius: 999px;
    color: var(--white);
    font-family: "Poppins", Arial, sans-serif;
    font-weight: 600;
    letter-spacing: 0.2px;
    white-space: nowrap;
  }
  .features { position: absolute; list-style: none; }
  .features li {
    position: relative;
    padding-left: 20px;
    font-style: italic;
    font-weight: 700;
    font-size: 14px;
    color: var(--ink);
    line-height: 1.2;
    margin-bottom: 6px;
  }
  .features li svg { position: absolute; left: 0; top: 4px; width: 11px; height: 10px; }
  .features li small { display: block; font-size: 10px; font-weight: 700; margin-top: 1px; }
</style>
</head>
<body>
<div class="sheet">

  <!-- Leaderboard -->
  <span class="size-label" style="left:70px; top:68px;">728×90</span>
  <section class="banner leaderboard" style="left:70px; top:85px; width:728px; height:90px;">
    <svg class="wave" viewBox="0 0 728 90" preserveAspectRatio="none" aria-hidden="true">
      <path d="M0,0 H220 C200,8 190,36 160,41 C110,47 50,54 0,66 Z"/>
      <path d="M425,90 C470,62 520,22 600,20 C660,18 700,14 728,6 V90 Z"/>
    </svg>
    <div class="ribbon" style="left:-14px; top:15px; width:110px; height:17px; font-size:8.5px; line-height:17px; transform:rotate(-36deg);">Affordable plan</div>
    <div class="price" style="left:82px; top:15px; font-size:27px;">$9.95</div>
    <div class="term" style="left:58px; top:48px; width:100px; text-align:center; font-size:10px; color:var(--ink);">a month<br>for 3 year term</div>
    <div class="headline" style="left:214px; top:15px; font-size:38px;"><span class="accent">Free</span> Printers</div>
    <div class="subline" style="left:200px; top:57px; font-size:11.5px;">Multifunction Monochrome Laser</div>
    <div class="printer-photo" role="img" aria-label="Photo of a white monochrome laser printer" style="left:466px; top:12px; width:92px; height:60px;"></div>
    <div class="cta" style="left:590px; top:28px; width:108px; height:33px; font-size:9.5px;">CLICK HERE</div>
  </section>

  <!-- Half page -->
  <span class="size-label" style="left:70px; top:202px;">300×600</span>
  <section class="banner half-page" style="left:70px; top:220px; width:300px; height:600px;">
    <svg class="wave" viewBox="0 0 300 600" preserveAspectRatio="none" aria-hidden="true">
      <path d="M0,0 H300 V145 C245,148 205,108 145,94 C95,83 45,82 0,92 Z"/>
      <path d="M0,498 C85,462 170,470 235,455 C268,447 288,438 300,430 V600 H0 Z"/>
    </svg>
    <div class="ribbon" style="left:-24px; top:40px; width:180px; height:28px; font-size:14px; line-height:28px; transform:rotate(-36deg);">Affordable plan</div>
    <div class="price" style="right:27px; top:24px; font-size:38px;">$9.95</div>
    <div class="term" style="right:29px; top:64px; text-align:right; font-size:14px; color:var(--white);">a month<br>for 3 year term</div>
    <div class="headline" style="left:34px; top:152px; font-size:46px;"><span class="accent">Free</span> Printers</div>
    <div class="subline" style="left:35px; top:201px; font-size:12px;">Multifunction Monochrome Laser</div>
    <ul class="features" style="left:35px; top:239px;">
      <li><svg viewBox="0 0 11 10" aria-hidden="true"><path d="M1,5 L4,8.5 L10,1" fill="none" stroke="#111" stroke-width="1.3"/></svg>Monochrome Printers<small>1000 prints per month</small></li>
      <li style="margin-top:10px;"><svg viewBox="0 0 11 10" aria-hidden="true"><path d="M1,5 L4,8.5 L10,1" fill="none" stroke="#111" stroke-width="1.3"/></svg>Toner included</li>
      <li><svg viewBox="0 0 11 10" aria-hidden="true"><path d="M1,5 L4,8.5 L10,1" fill="none" stroke="#111" stroke-width="1.3"/></svg>Service included</li>
      <li><svg viewBox="0 0 11 10" aria-hidden="true"><path d="M1,5 L4,8.5 L10,1" fill="none" stroke="#111" stroke-width="1.3"/></svg>Printer included</li>
    </ul>
    <div class="printer-photo" role="img" aria-label="Photo of a white monochrome laser printer" style="left:52px; top:377px; width:196px; height:122px;"></div>
    <div class="cta" style="left:70px; top:520px; width:160px; height:45px; font-size:13.5px;">CLICK HERE</div>
  </section>

  <!-- Medium rectangle -->
  <span class="size-label" style="left:414px; top:202px;">300×250</span>
  <section class="banner medium-rectangle" style="left:414px; top:220px; width:300px; height:250px;">
    <svg class="wave" viewBox="0 0 300 250" preserveAspectRatio="none" aria-hidden="true">
      <path d="M0,0 H300 V84 C245,94 200,58 140,58 C85,58 40,74 0,82 Z"/>
      <path d="M80,250 C125,205 195,186 300,180 V250 Z"/>
    </svg>
    <div class="ribbon" style="left:-12px; top:24px; width:140px; height:24px; font-size:10.5px; line-height:24px; transform:rotate(-36deg);">Affordable plan</div>
    <div class="price" style="right:17px; top:12px; font-size:32px;">$9.95</div>
    <div class="term" style="right:19px; top:45px; font-size:11.5px; color:var(--white);">a month for 3 year term</div>
    <div class="headline" style="left:21px; top:104px; font-size:34px; line-height:1.02;"><span class="accent">Free</span><br>Printers</div>
    <div class="subline" style="left:22px; top:177px; font-size:11.5px; line-height:1.45;">Multifunction<br>Monochrome<br>Laser</div>
    <div class="printer-photo" role="img" aria-label="Photo of a white monochrome laser printer" style="left:152px; top:97px; width:130px; height:80px;"></div>
    <div class="cta" style="left:176px; top:195px; width:108px; height:33px; font-size:9.5px;">CLICK HERE</div>
  </section>

  <!-- Small skyscraper -->
  <span class="size-label" style="left:414px; top:490px;">120×24</span>
  <section class="banner small-skyscraper" style="left:414px; top:508px; width:120px; height:240px;">
    <svg class="wave" viewBox="0 0 120 240" preserveAspectRatio="none" aria-hidden="true">
      <path d="M0,0 H120 V56 C92,62 70,42 42,44 C22,45 10,50 0,54 Z"/>
      <path d="M0,170 C30,192 82,188 120,164 V240 H0 Z"/>
    </svg>
    <div class="ribbon" style="left:-8px; top:14px; width:80px; height:15px; font-size:7px; line-height:15px; transform:rotate(-36deg);">Affordable plan</div>
    <div class="price" style="right:10px; top:17px; font-size:19px;">$9.95</div>
    <div class="headline" style="left:0; width:120px; text-align:center; top:56px; font-size:22px; line-height:1.05;"><span class="accent">Free</span><br>Printers</div>
    <div class="subline" style="left:0; width:120px; text-align:center; top:108px; font-size:7.5px;">Multifunction<br>Monochrome Laser</div>
    <div class="printer-photo" role="img" aria-label="Photo of a white monochrome laser printer" style="left:22px; top:142px; width:72px; height:44px;"></div>
    <div class="cta" style="left:22px; top:199px; width:76px; height:24px; font-size:6.5px; border-width:1.5px;">CLICK HERE</div>
  </section>

</div>
</body>
</html>
```